VelaTail, a CBD pet line, needs a label for its product.

We need a label for the bottle of our CBD (cannabidiol from hemp) tincture for pets (mainly cats and dogs). We want to incorporate the same blue and green color scheme that is found in our logo (attached) and would like it to have a pet feel, with a clean, professional design feel. Label size is 1.375" tall by 3.5" wide.
FRONT OF LABEL will need the following information: logo and pet friendly overall design. And the following wording: 450 mg, Pet Tincture, Premium Full Spectrum Hemp Extract, 0.5 fl oz 15ml.
BACK OF LABEL should include:
Suggested Use: For animal use only. Shake well before use. Store in a cool, dry place away from light. Pets under 30 lbs: Try 1 to 3 drops twice daily. Pets over 30 lbs: Try 4 to 8 drops twice daily. May be given orally or mixed in with food.
Ingredients: Whole plant hemp extract and MCT oil.
Hemp proudly grown in the USA.
www.KorvanHale.example
82 RR 5190 S, Bergheim, TX 78011
(830) 555-0147

```html
<!DOCTYPE html>
<html lang="en">
<head>
<meta charset="utf-8">
<title>VelaTail Pet Tincture Label</title>
<link href="https://fonts.googleapis.com/css2?family=Anton&family=Lato:wght@400;700;900&display=swap" rel="stylesheet">
<style>
  :root {
    --blue: #0f73c0;
    --blue-dark: #0a5b9c;
    --green: #7dc242;
    --white: #ffffff;
    --ink: #1d1d1d;
    --back-bg: #eef0f2;
    --placeholder: #d6d7d9;
    --strip: #c9ccd0;
    --page: #3a3b3d;
  }
  html, body {
    margin: 0;
    padding: 0;
    width: 971px;
    height: 1200px;
    overflow: hidden;
    background: var(--page);
  }
  .label {
    position: absolute;
    left: 25px;
    top: 418px;
    width: 977px;
    height: 387px;
    transform: scale(0.94);
    transform-origin: top left;
    overflow: hidden;
    background: var(--back-bg);
    box-shadow: 0 2px 6px rgba(0,0,0,.35);
    font-family: 'Lato', sans-serif;
  }
  .label-shapes { position: absolute; inset: 0; }
  .pet-photo {
    position: absolute;
    left: 262px;
    top: 170px;
    width: 150px;
    height: 217px;
    background: linear-gradient(160deg, #8a5a34 0%, #6b4226 45%, #e9e6e2 72%, #cfd3d8 100%);
    clip-path: polygon(18% 0, 100% 0, 100% 8%, 62% 100%, 0 100%, 0 22%);
  }
  .brand {
    position: absolute;
    font-family: 'Lato', sans-serif;
    font-weight: 400;
    color: var(--green);
    letter-spacing: -0.5px;
    margin: 0;
  }
  .brand-front { left: 42px; top: 14px; font-size: 40px; }
  .brand-back { left: 812px; top: 282px; font-size: 36px; }
  .front-title {
    position: absolute;
    left: 44px;
    top: 96px;
    margin: 0;
    font-family: 'Anton', sans-serif;
    font-weight: 400;
    font-size: 58px;
    line-height: 1;
    color: var(--green);
    letter-spacing: 0.5px;
  }
  .strength {
    position: absolute;
    left: 44px;
    top: 168px;
    width: 160px;
    height: 34px;
    background: var(--green);
    clip-path: polygon(0 0, 100% 0, 88% 100%, 0 100%);
    color: var(--white);
    font-family: 'Lato', sans-serif;
    font-weight: 900;
    font-size: 25px;
    line-height: 34px;
    padding-left: 10px;
    box-sizing: border-box;
  }
  .front-desc {
    position: absolute;
    left: 44px;
    top: 212px;
    margin: 0;
    font-family: 'Anton', sans-serif;
    font-size: 31px;
    line-height: 36px;
    color: var(--white);
    text-transform: uppercase;
  }
  .volume {
    position: absolute;
    left: 44px;
    top: 336px;
    margin: 0;
    font-family: 'Anton', sans-serif;
    font-size: 26px;
    color: var(--blue-dark);
  }
  .back-copy {
    position: absolute;
    left: 534px;
    top: 56px;
    margin: 0;
    font-size: 15.5px;
    line-height: 18.6px;
    color: var(--ink);
  }
  .back-copy .head { color: var(--blue); font-weight: 700; display: block; }
  .back-copy span { display: block; }
  .contact {
    position: absolute;
    left: 534px;
    top: 272px;
    margin: 0;
    font-style: normal;
    font-weight: 700;
    font-size: 15.5px;
    line-height: 18.6px;
    color: var(--blue);
  }
  .contact span { display: block; }
  .code-box {
    position: absolute;
    left: 850px;
    top: 38px;
    width: 108px;
    height: 228px;
    background: var(--placeholder);
  }
  .code-box span {
    position: absolute;
    left: 50%;
    top: 50%;
    transform: translate(-50%, -50%) rotate(-90deg);
    font-size: 13px;
    color: var(--ink);
    white-space: nowrap;
  }
</style>
</head>
<body>
  <div class="label">
    <svg class="label-shapes" viewBox="0 0 977 387" width="977" height="387" aria-hidden="true">
      <defs>
        <radialGradient id="backGlow" cx="0.6" cy="0.45" r="0.7">
          <stop offset="0" stop-color="#ffffff"/>
          <stop offset="1" stop-color="#e3e5e8"/>
        </radialGradient>
      </defs>
      <rect x="400" y="0" width="577" height="387" fill="url(#backGlow)"/>
      <polygon points="440,0 470,0 365,387 330,387" fill="var(--strip)"/>
      <polygon points="0,0 456,0 350,387 0,387" fill="var(--blue)"/>
      <path d="M0,0 H300 C270,0 262,78 222,80 H0 Z" fill="var(--white)"/>
      <path d="M0,332 H200 C230,332 236,310 262,300 L240,387 H0 Z" fill="var(--white)"/>
    </svg>

    <div class="pet-photo" role="img" aria-label="Photo of a brown boxer puppy sitting beside a white kitten"></div>

    <p class="brand brand-front">VelaTail</p>
    <h1 class="front-title">PET TINCTURE</h1>
    <div class="strength">450 mg</div>
    <p class="front-desc">Premium Full<br>Spectrum<br>Hemp Extract</p>
    <p class="volume">0.5 fl oz 15ml.</p>

    <p class="back-copy">
      <span class="head">Suggested Use:</span>
      <span>For animal use only. Shake well before use.</span>
      <span>Store in a cool, dry place away from light.</span>
      <span class="head">Pets under 30 lbs:</span>
      <span>Try 1 to 3 drops twice daily.</span>
      <span class="head">Pets over 30 lbs:</span>
      <span>Try 4 to 8 drops twice daily.</span>
      <span>May be given orally or mixed in with food.</span>
      <span class="head">Ingredients:</span>
      <span>Whole plant hemp extract and MCT oil.</span>
    </p>

    <address class="contact">
      <span>Hemp proudly grown in the USA.</span>
      <span>www.KorvanHale.example</span>
      <span>82 RR 5190 S, Bergheim, TX 78011</span>
      <span>(830) 555-0147</span>
    </address>

    <div class="code-box"><span>bar code</span></div>
    <p class="brand brand-back">VelaTail</p>
  </div>
</body>
</html>
```